Ferris Contracting LLC Business Card Design

I am looking for a creative and unique business card design. We are a commercial construction general contractor. With the name "FERRIS" Contracting, I am hoping to see some neat designs that correlate with the name.

```html
<!DOCTYPE html>
<html lang="en">
<head>
<meta charset="utf-8">
<title>Ferris Contracting LLC – Business Card</title>
<link href="https://fonts.googleapis.com/css2?family=Archivo:wght@400;800&display=swap" rel="stylesheet">
<style>
  :root {
    --blue: #1f8fd6;
    --blue-deep: #1677c0;
    --blue-light: #35a8e2;
    --ink: #2b2b2b;
    --grey-tab: #a9a7a9;
    --paper: #ffffff;
    --backdrop: #c4c4c4;
  }
  * { margin: 0; padding: 0; box-sizing: border-box; }
  html, body { width: 1200px; height: 800px; overflow: hidden; }
  body {
    background: var(--backdrop);
    font-family: "Archivo", Arial, sans-serif;
    position: relative;
  }
  .card {
    position: absolute;
    width: 560px;
    height: 320px;
    border-radius: 22px;
    overflow: hidden;
    box-shadow: 0 14px 30px rgba(0,0,0,0.25);
  }
  /* Front */
  .card-front { left: 40px; top: 70px; background: var(--paper); border-bottom: 3px solid var(--blue); }
  .corner-tab {
    position: absolute; right: 70px; top: 0;
    width: 66px; height: 48px; background: var(--grey-tab);
  }
  .person { position: absolute; left: 40px; top: 48px; }
  .person-name {
    font-weight: 800; font-size: 26px; letter-spacing: 0.5px;
    color: var(--blue-deep); text-transform: uppercase;
  }
  .person-title {
    font-weight: 400; font-size: 14px; letter-spacing: 0.5px;
    color: var(--ink); text-transform: uppercase; margin-top: 2px;
  }
  .contact-band {
    position: absolute; left: 0; top: 130px;
    width: 330px; height: 96px;
    background: linear-gradient(90deg, var(--blue-deep), var(--blue-light));
    padding: 12px 0 0 40px;
    color: #fff; font-size: 16px; line-height: 24px;
  }
  .contact-band li { list-style: none; display: flex; align-items: center; gap: 8px; }
  .contact-band svg { width: 14px; height: 14px; flex: none; }
  .address {
    position: absolute; left: 40px; top: 248px;
    font-size: 16px; line-height: 22px; color: var(--ink);
  }
  .front-wordmark {
    position: absolute; right: 44px; top: 120px;
    text-align: left;
    font-weight: 800; color: var(--blue);
    display: flex; align-items: center; gap: 12px;
  }
  .wordmark-dot { width: 18px; height: 18px; border-radius: 50%; background: var(--blue); flex: none; }
  .front-wordmark .wordmark-text { font-size: 44px; line-height: 1; letter-spacing: 1px; }
  .front-wordmark .wordmark-sub { display: block; font-size: 13px; letter-spacing: 6px; margin-top: 6px; }
  /* Back */
  .card-back {
    left: 600px; top: 410px;
    background: linear-gradient(160deg, var(--blue-light) 0%, var(--blue) 55%, var(--blue-deep) 100%);
  }
  .back-wordmark {
    position: absolute; left: 0; right: 0; top: 104px;
    text-align: center; color: #fff; font-weight: 800;
  }
  .back-wordmark .wordmark-text { font-size: 76px; line-height: 1; letter-spacing: 2px; display: block; }
  .back-wordmark .wordmark-sub { display: block; font-size: 18px; letter-spacing: 10px; margin-top: 8px; }
</style>
</head>
<body>
  <section class="card card-front" aria-label="Business card front">
    <div class="corner-tab"></div>
    <div class="person">
      <p class="person-name">Daniel Hayes</p>
      <p class="person-title">Managing Director</p>
    </div>
    <ul class="contact-band">
      <li>
        <svg viewBox="0 0 24 24" fill="#fff" aria-hidden="true"><path d="M6.6 10.8a15 15 0 0 0 6.6 6.6l2.2-2.2a1 1 0 0 1 1-.25 11.4 11.4 0 0 0 3.6.6 1 1 0 0 1 1 1V20a1 1 0 0 1-1 1A17 17 0 0 1 3 4a1 1 0 0 1 1-1h3.5a1 1 0 0 1 1 1c0 1.25.2 2.45.6 3.6a1 1 0 0 1-.25 1z"/></svg>
        044-555 019 284
      </li>
      <li>
        <svg viewBox="0 0 24 24" fill="#fff" aria-hidden="true"><path d="M2 5h20v14H2z M2 5l10 8 10-8" stroke="#1677c0" stroke-width="1.5"/></svg>
        info@ferrisbuild.com
      </li>
      <li>
        <svg viewBox="0 0 24 24" fill="none" stroke="#fff" stroke-width="2" aria-hidden="true"><circle cx="12" cy="12" r="9"/><path d="M3 12h18M12 3c3 3 3 15 0 18M12 3c-3 3-3 15 0 18"/></svg>
        www.ferrisbuild.com
      </li>
    </ul>
    <p class="address">210, Millstone Avenue<br>30617, Eastvale</p>
    <div class="front-wordmark">
      <span class="wordmark-dot"></span>
      <div><span class="wordmark-text">FERRIS</span><span class="wordmark-sub">CONTRACTING</span></div>
    </div>
  </section>

  <section class="card card-back" aria-label="Business card back">
    <div class="back-wordmark">
      <span class="wordmark-text">FERRIS</span>
      <span class="wordmark-sub">CONTRACTING</span>
    </div>
  </section>
</body>
</html>
```